Harbinger Slabworks, Inc. Business Card

Create a business card that is eye catching and based around concrete sawcutting. I've attached our current business card and logo for reference. We like aspects of the current business card, but it is starting to feel very loud and lost. We would like something that is still fun but is more modern and streamlined.

```html
<!DOCTYPE html>
<html lang="en">
<head>
<meta charset="utf-8">
<title>Harbinger Slabworks, Inc. Business Card</title>
<link href="https://fonts.googleapis.com/css2?family=Montserrat:wght@400;500;700;800&display=swap" rel="stylesheet">
<style>
  :root {
    --stage: #3a3431;
    --card-black: #000000;
    --card-grey: #8e9095;
    --accent-red: #d81f2a;
    --light-grey: #c9cacd;
    --text-white: #ffffff;
    --text-dark: #121212;
    --mark-navy: #23306b;
  }
  * { box-sizing: border-box; margin: 0; padding: 0; }
  html, body { width: 1200px; height: 786px; overflow: hidden; }
  body {
    background: var(--stage);
    font-family: "Montserrat", sans-serif;
    position: relative;
  }
  .card {
    position: absolute;
    top: 238px;
    width: 540px;
    height: 309px;
    overflow: hidden;
    box-shadow: 0 14px 30px rgba(0,0,0,0.45);
  }
  .card--front { left: 40px; background: var(--card-black); }
  .card--back { left: 620px; background: var(--card-grey); }

  .brand {
    position: absolute;
    display: flex;
    align-items: center;
    gap: 10px;
    width: 170px;
  }
  .brand__dot {
    flex: 0 0 34px;
    height: 34px;
    border-radius: 50%;
    background: var(--accent-red);
  }
  .brand__name {
    font-weight: 700;
    font-size: 17px;
    line-height: 1.15;
    color: var(--text-white);
    text-transform: uppercase;
  }
  .card--front .brand { left: 30px; top: 118px; }
  .card--back .brand { left: 100px; top: 118px; }

  .divider {
    position: absolute;
    width: 2px;
    background: var(--accent-red);
  }
  .card--front .divider { left: 222px; top: 50px; height: 150px; }
  .card--back .divider { left: 290px; top: 78px; height: 140px; }

  .contact { position: absolute; left: 240px; top: 46px; color: var(--text-white); }
  .contact__name {
    color: var(--accent-red);
    font-weight: 800;
    font-size: 22px;
    margin-bottom: 16px;
  }
  .contact__address { font-size: 13px; line-height: 1.35; margin-bottom: 12px; }
  .contact__line {
    display: flex;
    align-items: center;
    gap: 10px;
    font-size: 13px;
    margin-bottom: 7px;
  }
  .contact__icon { width: 14px; height: 14px; flex: 0 0 14px; }

  .bands { position: absolute; left: 0; bottom: 0; width: 540px; height: 40px; }

  .services { position: absolute; left: 308px; top: 78px; }
  .services__phone {
    color: var(--accent-red);
    font-weight: 700;
    font-size: 19px;
    margin-bottom: 10px;
  }
  .services__list { list-style: none; }
  .services__item {
    font-size: 12.5px;
    color: var(--text-dark);
    text-transform: uppercase;
    margin-bottom: 6px;
    display: flex;
    align-items: center;
    gap: 7px;
  }
  .services__item::before {
    content: "";
    width: 5px; height: 5px;
    border-radius: 50%;
    background: var(--accent-red);
  }
</style>
</head>
<body>
  <section class="card card--front" aria-label="Business card front">
    <div class="brand">
      <span class="brand__dot"></span>
      <span class="brand__name">Harbinger Slabworks, Inc.</span>
    </div>
    <div class="divider"></div>
    <div class="contact">
      <p class="contact__name">Marisa Kellner</p>
      <p class="contact__address">48 N. Alder Row<br>Fairhaven, NJ 07590</p>
      <p class="contact__line">
        <svg class="contact__icon" viewBox="0 0 16 16"><path fill="#d81f2a" d="M2 6c0-2 2.5-3 6-3s6 1 6 3l-2 1-1.5-1.8V4.5h-5v.7L4 7z M4 9l2-3h4l2 3v4H4z"/></svg>
        855. 555. 0142
      </p>
      <p class="contact__line">
        <svg class="contact__icon" viewBox="0 0 16 16"><rect x="4" y="1" width="8" height="14" rx="1.5" fill="none" stroke="#d81f2a" stroke-width="1.6"/><circle cx="8" cy="12.5" r="0.9" fill="#d81f2a"/></svg>
        973. 555. 0186
      </p>
      <p class="contact__line">
        <svg class="contact__icon" viewBox="0 0 16 16"><rect x="1" y="3" width="14" height="10" fill="#d81f2a"/><path d="M1 3l7 6 7-6" fill="none" stroke="#000" stroke-width="1.2"/></svg>
        marisa@harbingerslabworks
      </p>
    </div>
    <svg class="bands" viewBox="0 0 540 40" preserveAspectRatio="none">
      <polygon points="0,24 318,24 306,40 0,40" fill="#d81f2a"/>
      <polygon points="330,16 540,16 540,30 322,30" fill="#c9cacd"/>
    </svg>
  </section>

  <section class="card card--back" aria-label="Business card back">
    <div class="brand">
      <span class="brand__dot"></span>
      <span class="brand__name">Harbinger Slabworks, Inc.</span>
    </div>
    <div class="divider"></div>
    <div class="services">
      <p class="services__phone">855-SLAB CUT</p>
      <ul class="services__list">
        <li class="services__item">Wall Sawing</li>
        <li class="services__item">Core Drilling</li>
        <li class="services__item">Slab Sawing</li>
        <li class="services__item">Breaking &amp; Removal</li>
      </ul>
    </div>
  </section>
</body>
</html>
```